BrightWink Boothery Business Card Design Project

BrightWink Boothery requires a business card design. We hire PhotoBooths to events such as Birthday Parties, Hens and Bucks Night, Anniversaries, Corporate Functions
, Engagements, Theme Nights, Presentation Night etc.
Business Card needs to look Modern, Professional And Catchy.
Updates

Hello Thankyou for all of your great designs, contact information will be provided shortly. We are considering the front of the card to be white themed and the back of the card to be black themed. And all social media colours to be their original colour. Thankyou

Hello everyone, Here are the contact details: Colin Marsh - Manager Mobile number - 0491838047 Website - www.brightwinkboothery.com Email - admin@brightwinkboothery.com And if you can add the word "weddings" in the "We cater For" section would be good. Thankyou

Target Market(s)

Birthday Parties
Hens and Bucks Night
Weddings
Corporate Functions
Engagements
Theme Nights
Presentation Night
School Functions

Industry/Entity Type

Events

Requirements
Must have
• Must Match Logo
Must Have www.brightwinkboothery.com

On Back of card must have social media icons Friendbook, Chirper, ClipTube, Linkin and

We Cater For:

Birthday Parties
Hens and Bucks Night
Anniversaries
Corporate Functions
Engagements
Theme Nights
Presentation Night
School Functions
And more.....

```html
<!DOCTYPE html>
<html lang="en">
<head>
<meta charset="utf-8">
<title>BrightWink Boothery – Business Card Back</title>
<link rel="stylesheet" href="https://fonts.googleapis.com/css2?family=Mulish:wght@300;400;800&display=swap">
<style>
  :root {
    --card-bg: #ffffff;
    --brand-cyan: #44e4ea;
  }
  html, body {
    margin: 0;
    padding: 0;
    width: 1200px;
    height: 741px;
    overflow: hidden;
    background: var(--card-bg);
  }
  .card {
    display: block;
    width: 1200px;
    height: 741px;
  }
  .frame-corner { fill: var(--brand-cyan); }
  .card-text {
    font-family: "Mulish", sans-serif;
    fill: var(--brand-cyan);
    text-anchor: middle;
  }
  .contact-name, .contact-address { font-size: 24px; font-weight: 300; }
  .cater-heading { font-size: 28px; font-weight: 800; }
  .cater-item { font-size: 29px; font-weight: 300; }
  .contact-line { font-size: 24px; font-weight: 300; }
  .social-square { fill: var(--brand-cyan); }
  .social-label { font-size: 14px; font-weight: 400; text-anchor: start; }
</style>
</head>
<body>
<svg class="card" viewBox="0 0 1100 690" preserveAspectRatio="none" role="img" aria-label="BrightWink Boothery business card, back">
  <g class="outer-frame">
    <rect class="frame-corner" x="147" y="75" width="134" height="15"/>
    <rect class="frame-corner" x="147" y="75" width="15" height="118"/>
    <rect class="frame-corner" x="851" y="71" width="134" height="15"/>
    <rect class="frame-corner" x="969" y="71" width="16" height="118"/>
    <rect class="frame-corner" x="135" y="487" width="16" height="118"/>
    <rect class="frame-corner" x="135" y="590" width="134" height="15"/>
    <rect class="frame-corner" x="964" y="494" width="16" height="118"/>
    <rect class="frame-corner" x="846" y="597" width="134" height="15"/>
  </g>
  <g class="inner-frame">
    <rect class="frame-corner" x="295" y="151" width="89" height="9"/>
    <rect class="frame-corner" x="295" y="151" width="10" height="78"/>
    <rect class="frame-corner" x="762" y="148" width="89" height="9"/>
    <rect class="frame-corner" x="841" y="148" width="10" height="78"/>
    <rect class="frame-corner" x="288" y="424" width="10" height="78"/>
    <rect class="frame-corner" x="288" y="493" width="88" height="9"/>
    <rect class="frame-corner" x="837" y="429" width="10" height="78"/>
    <rect class="frame-corner" x="759" y="498" width="88" height="9"/>
  </g>

  <text class="card-text contact-name" x="559" y="113">John Doe</text>
  <text class="card-text contact-address" x="564" y="148">Address:</text>

  <text class="card-text cater-heading" x="569" y="199">We Cater For:</text>
  <g class="cater-list">
    <text class="card-text cater-item" x="569" y="229">Birthday Parties</text>
    <text class="card-text cater-item" x="569" y="258">Hens and Bucks Night</text>
    <text class="card-text cater-item" x="569" y="287">Anniversaries</text>
    <text class="card-text cater-item" x="569" y="316">Corporate Functions</text>
    <text class="card-text cater-item" x="569" y="345">Engagements</text>
    <text class="card-text cater-item" x="569" y="374">Theme Nights</text>
    <text class="card-text cater-item" x="569" y="403">Presentation Night</text>
    <text class="card-text cater-item" x="569" y="432">School Functions</text>
    <text class="card-text cater-item" x="569" y="461">And more.....</text>
  </g>

  <text class="card-text contact-line" x="574" y="513">Phone:xxx.xxx.xxx</text>
  <text class="card-text contact-line" x="585" y="541">www.brightwinkboothery.com</text>

  <g class="social-links">
    <rect class="social-square" x="418" y="570" width="10" height="10"/>
    <text class="card-text social-label" x="432" y="580">Friendbook</text>
    <rect class="social-square" x="510" y="570" width="10" height="10"/>
    <text class="card-text social-label" x="524" y="580">Chirper</text>
    <rect class="social-square" x="585" y="570" width="10" height="10"/>
    <text class="card-text social-label" x="599" y="580">ClipTube</text>
    <rect class="social-square" x="666" y="570" width="10" height="10"/>
    <text class="card-text social-label" x="680" y="580">WorkLink</text>
  </g>
</svg>
</body>
</html>
```